photowall advertisement

We require a wall featuring our company logo. We would like to avoid the color green, and gold is highly preferred. The design should be similar to the one in the attached photo. The wall will be used for photos and promotional purposes during congresses. Files must be prepared for printing.
dimension of wall: 470x223 cm

Industry/Entity Type

lifestyle

Colors
0054AA
0677BA
7BADD7
CADEEF
E8F1F8
6B429C
8869AF
B7A5CE
E3DAEB
F3F0F8

Requirements
Must have
• gold color, white, and other compare with gold color
Nice to have
• some pictograms, maps of Europe

```html
<!DOCTYPE html>
<html lang="en">
<head>
<meta charset="utf-8">
<title>Bright Arc – Photowall</title>
<link rel="stylesheet" href="https://fonts.googleapis.com/css2?family=Saira+Condensed:wght@500;600&display=swap">
<style>
  :root {
    --page-bg: #cfcfcf;
    --wall-bg: #ffffff;
    --crimson: #8c1a2c;
    --gold: #b8903f;
    --tile-bg: #ffffff;
    --tile-edge: #e4e4e4;
    --map-tone: #e9e9e9;
    --band-text: #ffffff;
  }
  * { box-sizing: border-box; margin: 0; padding: 0; }
  html, body {
    width: 910px;
    height: 1200px;
    overflow: hidden;
    background: var(--page-bg);
    font-family: "Saira Condensed", "Arial Narrow", sans-serif;
  }
  .photowall {
    position: absolute;
    left: 30px;
    top: 398px;
    width: 850px;
    height: 403px;
    background: var(--wall-bg);
    overflow: hidden;
  }
  .europe-map {
    position: absolute;
    left: 100px;
    top: 0;
    width: 580px;
    height: 403px;
    background: radial-gradient(ellipse at 55% 50%, var(--map-tone) 0%, rgba(233,233,233,0.55) 45%, rgba(255,255,255,0) 72%);
  }
  .logo-tile {
    position: absolute;
    background: var(--tile-bg);
    border: 1px solid var(--tile-edge);
    border-radius: 2px;
    box-shadow: 0 1px 3px rgba(0,0,0,0.12);
    display: flex;
    align-items: center;
    justify-content: center;
    color: var(--crimson);
    font-weight: 600;
    letter-spacing: 1.5px;
  }
  .logo-tile--wide {
    width: 190px;
    height: 46px;
    gap: 10px;
    font-size: 22px;
  }
  .logo-tile--stacked {
    width: 131px;
    height: 61px;
    flex-direction: column;
    gap: 4px;
    font-size: 19px;
  }
  .logo-mark {
    display: block;
    width: 14px;
    height: 14px;
    background: var(--gold);
  }
  .logo-tile--stacked .logo-mark { width: 16px; height: 16px; }
  .url-band {
    position: absolute;
    left: 0;
    top: 300px;
    width: 850px;
    height: 28px;
    background: var(--crimson);
  }
  .url-band__link {
    position: absolute;
    top: 4px;
    transform: translateX(-50%);
    color: var(--band-text);
    font-size: 14px;
    font-weight: 500;
    white-space: nowrap;
  }
</style>
</head>
<body>
  <main class="photowall">
    <div class="europe-map" role="img" aria-label="Faint dotted map of Europe in the background"></div>

    <!-- row 1 -->
    <div class="logo-tile logo-tile--wide" style="left:26px;top:28px"><span class="logo-mark"></span>BRIGHT ARC</div>
    <div class="logo-tile logo-tile--wide" style="left:229px;top:28px"><span class="logo-mark"></span>BRIGHT ARC</div>
    <div class="logo-tile logo-tile--wide" style="left:432px;top:28px"><span class="logo-mark"></span>BRIGHT ARC</div>
    <div class="logo-tile logo-tile--wide" style="left:634px;top:28px"><span class="logo-mark"></span>BRIGHT ARC</div>

    <!-- row 2 -->
    <div class="logo-tile logo-tile--stacked" style="left:54px;top:87px"><span class="logo-mark"></span>BRIGHT ARC</div>
    <div class="logo-tile logo-tile--stacked" style="left:258px;top:87px"><span class="logo-mark"></span>BRIGHT ARC</div>
    <div class="logo-tile logo-tile--stacked" style="left:462px;top:87px"><span class="logo-mark"></span>BRIGHT ARC</div>
    <div class="logo-tile logo-tile--stacked" style="left:665px;top:87px"><span class="logo-mark"></span>BRIGHT ARC</div>

    <!-- row 3 -->
    <div class="logo-tile logo-tile--wide" style="left:26px;top:162px"><span class="logo-mark"></span>BRIGHT ARC</div>
    <div class="logo-tile logo-tile--wide" style="left:229px;top:162px"><span class="logo-mark"></span>BRIGHT ARC</div>
    <div class="logo-tile logo-tile--wide" style="left:432px;top:162px"><span class="logo-mark"></span>BRIGHT ARC</div>
    <div class="logo-tile logo-tile--wide" style="left:634px;top:162px"><span class="logo-mark"></span>BRIGHT ARC</div>

    <!-- row 4 -->
    <div class="logo-tile logo-tile--stacked" style="left:54px;top:222px"><span class="logo-mark"></span>BRIGHT ARC</div>
    <div class="logo-tile logo-tile--stacked" style="left:258px;top:222px"><span class="logo-mark"></span>BRIGHT ARC</div>
    <div class="logo-tile logo-tile--stacked" style="left:462px;top:222px"><span class="logo-mark"></span>BRIGHT ARC</div>
    <div class="logo-tile logo-tile--stacked" style="left:665px;top:222px"><span class="logo-mark"></span>BRIGHT ARC</div>

    <div class="url-band">
      <span class="url-band__link" style="left:120px">www.brightarcstudio.com</span>
      <span class="url-band__link" style="left:425px">www.brightarcstudio.com</span>
      <span class="url-band__link" style="left:730px">www.brightarcstudio.com</span>
    </div>
  </main>
</body>
</html>
```